Industrial Rubber Manufacturer Trade-Show Flyer

We are looking for a flyer to hand out to potential customers while walking the floors of a trade show. I have attached a document coming several of the product lines we currently do. Please refer to our website www.corvanpolymers.com for the color we are looking for the gold, brownish, and black colors in our header. I don't have any pictures besides our one of the building. We would like to have rubber extrusion related pictures and / or displays of industries we sell to
Target Market(s)
automotive, rv industry
Industry/Entity Type
Industrial
Font styles to use
Requirements
Must have
- clean look and feel. display information about the company.

```html
<!DOCTYPE html>
<html lang="en">
<head>
<meta charset="utf-8">
<title>Corvan Polymers – Trade-Show Flyer</title>
<link rel="stylesheet" href="https://fonts.googleapis.com/css2?family=Oswald:wght@400;500;600&display=swap">
<style>
  :root{
    --red:#c21f2b;
    --red-bright:#e63a2c;
    --orange:#f0941d;
    --ink:#3b3b3d;
    --cream:#f6f1e8;
    --brown-dark:#5b4b43;
    --brown-mid:#8e7b6e;
    --beige:#cbbb9e;
    --tan-bg:#c9a97c;
  }
  *{box-sizing:border-box;margin:0;padding:0}
  html,body{width:1200px;height:1200px;overflow:hidden;background:#fff}
  body{position:relative;font-family:"Oswald",sans-serif;color:var(--ink)}

  .flyer{
    position:absolute;left:180px;width:1015px;height:599px;
    transform-origin:0 0;transform:scale(0.879);
    overflow:hidden;box-shadow:0 2px 6px rgba(0,0,0,.35);
  }
  .flyer--front{top:51px;background:linear-gradient(180deg,#b9c0c6 0%,#d6d3cb 45%,#e6dccb 100%)}
  .flyer--back{top:612px;height:597px;background:linear-gradient(90deg,#9a8e79 0%,#cfbc9f 45%,#d9b98c 100%)}
  .photos{position:absolute;inset:0;width:100%;height:100%}

  .brand-line{position:absolute;right:15px;top:62px;font-size:50px;font-weight:500;letter-spacing:-.5px;line-height:1;white-space:nowrap}
  .brand-line .accent{color:var(--red)}
  .brand-line .dark{color:var(--ink)}
  .tagline{
    position:absolute;right:0;top:118px;width:380px;height:48px;background:var(--red-bright);
    clip-path:polygon(5% 0,100% 0,100% 100%,0 100%);
    color:#fff;font-size:14px;line-height:23px;text-align:right;padding:1px 16px 0 0;white-space:nowrap;
  }

  .info-box{position:absolute;background:linear-gradient(135deg,#fbf8f2,#efe7da);box-shadow:0 2px 5px rgba(0,0,0,.35)}
  .info-box__head{background:var(--red);color:#fff;font-size:28px;font-weight:500;line-height:1;padding:12px 0 0;height:52px;text-align:center;white-space:nowrap;letter-spacing:-.3px}
  .info-box__head--compact{font-size:23px;padding-top:13px}
  .info-box__list{list-style:none;padding:12px 0 0 22px;font-size:16px;line-height:24px;color:#2e2e2e;white-space:nowrap}
  .info-box__list li::before{content:"•";margin-right:7px}

  .tag{position:absolute;font-size:15px;color:#fff;line-height:24px;white-space:nowrap}
  .tag--address{left:260px;top:398px;width:200px;height:74px;background:var(--brown-dark);clip-path:polygon(0 0,100% 0,88% 50%,100% 100%,0 100%);padding:12px 0 0 12px}
  .tag--web{left:260px;top:478px;width:252px;height:50px;background:var(--brown-mid);clip-path:polygon(0 0,92% 0,100% 100%,0 100%);padding:13px 0 0 12px;color:#eee3d6}
  .tag--mail{left:260px;top:530px;width:282px;height:46px;background:var(--beige);clip-path:polygon(0 0,92% 0,100% 100%,0 100%);padding:11px 0 0 12px;color:#5c4e45}

  .brand-stack{position:absolute;right:293px;top:384px;text-align:right;font-weight:500;line-height:.92;letter-spacing:-1px;white-space:nowrap}
  .brand-stack .accent{display:block;color:var(--red);font-size:106px}
  .brand-stack .dark{display:block;color:var(--ink);font-size:106px}

  .ribbon{position:absolute;right:0;color:#fff;font-size:15px;line-height:24px;text-align:right;padding-right:16px;white-space:nowrap}
  .ribbon--address{top:408px;width:182px;height:74px;background:var(--red);clip-path:polygon(0 0,100% 0,100% 100%,6% 100%,14% 50%);padding-top:12px}
  .ribbon--web{top:463px;width:236px;height:70px;background:var(--red-bright);clip-path:polygon(0 30%,100% 0,100% 100%,0 100%);padding-top:30px}
  .ribbon--mail{top:510px;width:276px;height:76px;background:var(--orange);clip-path:polygon(0 30%,100% 20%,100% 100%,6% 100%,0 100%);padding-top:37px}
</style>
</head>
<body>

<section class="flyer flyer--front">
  <svg class="photos" viewBox="0 0 1015 599" preserveAspectRatio="none">
    <defs>
      <linearGradient id="gBuilding" x1="0" y1="0" x2="0" y2="1"><stop offset="0" stop-color="#c4c8cb"/><stop offset="1" stop-color="#ddd2bf"/></linearGradient>
      <linearGradient id="gWorker" x1="0" y1="0" x2="1" y2="1"><stop offset="0" stop-color="#3a3f52"/><stop offset=".5" stop-color="#2345a8"/><stop offset="1" stop-color="#5a5e66"/></linearGradient>
      <linearGradient id="gTires" x1="0" y1="0" x2="1" y2="1"><stop offset="0" stop-color="#2a2a2a"/><stop offset="1" stop-color="#5a5a5a"/></linearGradient>
      <linearGradient id="gFoam" x1="0" y1="0" x2="1" y2="1"><stop offset="0" stop-color="#2a4f9a"/><stop offset="1" stop-color="#1d3470"/></linearGradient>
      <linearGradient id="gGloves" x1="0" y1="0" x2="0" y2="1"><stop offset="0" stop-color="#3b9bd3"/><stop offset=".5" stop-color="#c1272f"/><stop offset="1" stop-color="#9b1e28"/></linearGradient>
    </defs>
    <rect x="460" y="160" width="555" height="439" fill="url(#gBuilding)" opacity=".6" role="img" aria-label="Photo of the factory building"/>
    <polygon points="0,0 330,0 330,290 0,112" fill="url(#gWorker)" role="img" aria-label="Photo of a worker with a tablet among tire racks"/>
    <polygon points="0,118 322,298 258,333 0,474" fill="url(#gTires)" role="img" aria-label="Photo of stacked rubber tires"/>
    <polygon points="0,480 258,338 258,599 0,599" fill="url(#gFoam)" role="img" aria-label="Photo of a rolled blue foam sheet"/>
    <polygon points="337,0 660,178 337,355" fill="url(#gGloves)" role="img" aria-label="Photo of colourful rubber gloves"/>
    <g stroke="#7a5a3c" stroke-width="4" fill="none">
      <line x1="335" y1="0" x2="335" y2="357"/><line x1="337" y1="355" x2="662" y2="178"/>
      <line x1="0" y1="115" x2="326" y2="297"/><line x1="0" y1="477" x2="260" y2="335"/><line x1="260" y1="335" x2="260" y2="599"/>
    </g>
  </svg>

  <h1 class="brand-line"><span class="accent">CORVAN</span> <span class="dark">POLYMERS</span></h1>
  <p class="tagline">We specialize in the custom design and production of both<br>closed cell sponge and solid rubber &amp; plastic extrusions</p>

  <div class="info-box" style="left:548px;top:298px;width:212px;height:205px">
    <h2 class="info-box__head">KEY PRODUCTS</h2>
    <ul class="info-box__list"><li>RV Sealing Products</li><li>Gaskets &amp; Seals</li><li>Tubes &amp; Protector Sleeves</li><li>Anti-Vibration Pads</li><li>Weather-Stripping</li></ul>
  </div>
  <div class="info-box" style="left:772px;top:250px;width:238px;height:295px">
    <h2 class="info-box__head info-box__head--compact">MATERIAL SPECIALTY</h2>
    <ul class="info-box__list"><li>EPDM (Dense / Sponge)</li><li>Silicone</li><li>Nitrile</li><li>Neoprene</li><li>SBR</li><li>Polyisoprene</li><li>Dual Duro</li><li>TPV / TPE / TPV</li><li>PVC (Flexible)</li></ul>
  </div>

  <div class="tag tag--address">4810 County Road 12<br>Millbrook, OH 44390</div>
  <div class="tag tag--web">www.corvanpolymers.com</div>
  <div class="tag tag--mail">info@corvanpolymers.com</div>
</section>

<section class="flyer flyer--back">
  <svg class="photos" viewBox="0 0 1015 597" preserveAspectRatio="none">
    <defs>
      <linearGradient id="gAerial" x1="0" y1="0" x2="1" y2="1"><stop offset="0" stop-color="#a59a86"/><stop offset="1" stop-color="#7c7463"/></linearGradient>
      <linearGradient id="gTires2" x1="0" y1="0" x2="1" y2="1"><stop offset="0" stop-color="#4a2a2e"/><stop offset="1" stop-color="#7a4a4e"/></linearGradient>
      <linearGradient id="gFoam2" x1="0" y1="0" x2="1" y2="1"><stop offset="0" stop-color="#4a4570"/><stop offset="1" stop-color="#6a63a0"/></linearGradient>
    </defs>
    <polygon points="170,260 600,180 620,597 170,597" fill="url(#gAerial)" opacity=".55" role="img" aria-label="Aerial photo of the factory site"/>
    <polygon points="0,0 232,0 232,270 0,132" fill="url(#gWorker)" role="img" aria-label="Photo of a worker with a tablet among tire racks"/>
    <polygon points="0,138 232,276 166,305 0,380" fill="url(#gTires2)" role="img" aria-label="Photo of stacked rubber tires"/>
    <polygon points="0,386 166,310 166,597 0,597" fill="url(#gFoam2)" role="img" aria-label="Photo of a rolled foam sheet"/>
    <polygon points="246,0 570,152 246,336" fill="url(#gGloves)" role="img" aria-label="Photo of colourful rubber gloves"/>
    <g stroke="#e0262c" stroke-width="5" fill="none">
      <line x1="244" y1="0" x2="244" y2="338"/><line x1="246" y1="336" x2="572" y2="152"/>
      <line x1="0" y1="135" x2="234" y2="273"/><line x1="0" y1="383" x2="168" y2="307"/>
    </g>
  </svg>

  <div class="info-box" style="left:578px;top:110px;width:214px;height:245px">
    <h2 class="info-box__head info-box__head--compact">INDUSTRIES SERVER</h2>
    <ul class="info-box__list"><li>Recreational Vehicles</li><li>Industrial</li><li>Automotive</li><li>Window &amp; Door</li><li>Agriculture</li><li>Heavy Equipment</li><li>Electrical &amp; Lighting</li></ul>
  </div>
  <div class="info-box" style="left:802px;top:98px;width:198px;height:272px">
    <h2 class="info-box__head info-box__head--compact">TOOLS &amp; SERVICES</h2>
    <ul class="info-box__list"><li>Tool &amp; Die Shop</li><li>Cutting</li><li>Taping</li><li>hole punch</li><li>Notching</li><li>Retail Packaging</li><li>Vulcanized Splicing</li><li>Flocking</li></ul>
  </div>

  <h1 class="brand-stack"><span class="accent">CORVAN</span><span class="dark">POLYMERS</span></h1>

  <div class="ribbon ribbon--mail">info@corvanpolymers.com</div>
  <div class="ribbon ribbon--web">www.corvanpolymers.com</div>
  <div class="ribbon ribbon--address">4810 County Road 12<br>Millbrook, OH 44390</div>
</section>

</body>
</html>
```